Morden, Creative, Unique, Independent Wine Shop

1. We are a brand new wine shop located in Melbourne Australia, we have our logo already, simply use the logo to design a business card.
2. I have uploaded our logo in two versions, with or without shadow, any of them is acceptable.
3. Make it as creative and unique as possible, no limitation of shape, color combination, geometry pattern, fonts, composing etc.
3. Info on the card:
- Brambleford Wine Cellar (Not very necessary if logo is obviously shown)
- 42 Ferncastle Steet, Marrowdale, Wenford, Australia 3291
- +61 3 9018 4637
- www.bramblefordwinecellar.com.au
- bramblefordwinecellar@mailvista.com
- Additional icons: Google, Instagram, Facebook, Twitter
4. Once again, forget it is a commercial card, make it special.

```html
<!DOCTYPE html>
<html lang="en">
<head>
<meta charset="utf-8">
<title>Brambleford Wine Cellar – Business Card</title>
<link rel="stylesheet" href="https://fonts.googleapis.com/css2?family=Cinzel:wght@500&family=Tinos&family=Arimo&display=swap">
<style>
  :root {
    --backdrop: #3a2a1e;
    --card: #ffffff;
    --wine: #7d1518;
    --slate: #6b6b6b;
    --label: #ffffff;
    --faint: #f1f1f1;
  }
  * { margin: 0; padding: 0; box-sizing: border-box; }
  html, body { width: 1200px; height: 1200px; overflow: hidden; }
  body { background: var(--backdrop); position: relative; }

  .side-label {
    position: absolute; left: 65px;
    font-family: "Arimo", Arial, sans-serif;
    font-size: 54px; color: var(--label); letter-spacing: 1px;
  }
  .side-label.front { top: 188px; }
  .side-label.back { top: 786px; }

  .card {
    position: absolute; left: 295px; width: 620px; height: 354px;
    background: var(--card); overflow: hidden;
  }
  .card.front { top: 124px; }
  .card.back { top: 734px; }
  .card svg.shapes { position: absolute; inset: 0; }

  .brand {
    position: absolute; display: flex; align-items: center; gap: 14px;
    font-family: "Cinzel", Georgia, serif; font-weight: 500; color: var(--wine);
  }
  .brand .dot { width: 40px; height: 40px; border-radius: 50%; background: var(--wine); flex: none; }
  .brand .name { line-height: 1.05; }
  .brand .name .main { display: block; font-size: 34px; }
  .brand .name .sub { display: block; font-size: 15px; letter-spacing: 3px; padding-left: 40px; }
  .front .brand { left: 28px; top: 72px; }

  .contact {
    position: absolute; left: 24px; top: 207px; list-style: none;
    font-family: "Tinos", "Times New Roman", serif; font-size: 13.5px; color: #fff;
  }
  .contact li { display: flex; align-items: center; gap: 5px; height: 30px; }
  .contact svg { width: 20px; height: 20px; flex: none; }

  .back .brand { left: 0; right: 0; top: 108px; justify-content: center; }
  .back .brand .name { text-align: center; }
  .back .brand .name .sub { padding-left: 0; }
  .back .site {
    position: absolute; left: 0; right: 0; top: 314px; text-align: center;
    font-family: "Tinos", "Times New Roman", serif; font-size: 13.5px; color: #fff;
  }
</style>
</head>
<body>
  <div class="side-label front">FRONT</div>
  <div class="side-label back">BACK</div>

  <section class="card front">
    <svg class="shapes" width="620" height="354" viewBox="0 0 620 354">
      <circle class="faint-mark" cx="540" cy="180" r="120" fill="var(--faint)"/>
      <polygon class="info-band" points="0,187 413,187 250,354 0,354" fill="var(--wine)"/>
      <polygon class="chevron-slate" points="297,0 315,0 470,176 300,354 283,354 455,176" fill="var(--slate)"/>
      <polygon class="chevron-wine" points="330,0 370,0 545,176 372,354 312,354 495,176" fill="var(--wine)"/>
    </svg>

    <div class="brand">
      <span class="dot"></span>
      <span class="name"><span class="main">Brambleford</span><span class="sub">WINE CELLAR</span></span>
    </div>

    <ul class="contact">
      <li>
        <svg viewBox="0 0 20 20"><circle cx="10" cy="10" r="10" fill="#fff"/><path d="M10 4.5a3.6 3.6 0 0 0-3.6 3.6c0 2.7 3.6 7 3.6 7s3.6-4.3 3.6-7A3.6 3.6 0 0 0 10 4.5z" fill="var(--wine)"/><circle cx="10" cy="8.1" r="1.4" fill="#fff"/></svg>
        42 Ferncastle Steet, Marrowdale, Wenford, Australia 3291
      </li>
      <li>
        <svg viewBox="0 0 20 20"><circle cx="10" cy="10" r="10" fill="#fff"/><path d="M6.4 5.2l2 .1.9 2.4-1.2 1a6.5 6.5 0 0 0 3.2 3.2l1-1.2 2.4.9.1 2c-.1.6-.7 1-1.3 1A8.5 8.5 0 0 1 5.4 6.5c0-.6.4-1.2 1-1.3z" fill="var(--wine)"/></svg>
        +61 3 9018 4637
      </li>
      <li>
        <svg viewBox="0 0 20 20"><circle cx="10" cy="10" r="10" fill="#fff"/><g fill="none" stroke="var(--wine)" stroke-width="1.1"><circle cx="10" cy="10" r="5.5"/><ellipse cx="10" cy="10" rx="2.3" ry="5.5"/><path d="M4.5 10h11M5.3 7.3h9.4M5.3 12.7h9.4"/></g></svg>
        www.bramblefordwinecellar.com.au
      </li>
      <li>
        <svg viewBox="0 0 20 20"><circle cx="10" cy="10" r="10" fill="#fff"/><rect x="5" y="6.5" width="10" height="7" rx="1" fill="var(--wine)"/><path d="M5.3 7l4.7 3.6L14.7 7" fill="none" stroke="#fff" stroke-width="1"/></svg>
        bramblefordwinecellar@mailvista.com
      </li>
    </ul>
  </section>

  <section class="card back">
    <svg class="shapes" width="620" height="354" viewBox="0 0 620 354">
      <rect class="rule-slate" x="0" y="264" width="620" height="14" fill="var(--slate)"/>
      <rect class="footer-band" x="0" y="286" width="620" height="68" fill="var(--wine)"/>
    </svg>
    <div class="brand">
      <span class="name"><span class="main">Brambleford</span><span class="sub">WINE CELLAR</span></span>
    </div>
    <div class="site">www.bramblefordwinecellar.com.au</div>
  </section>
</body>
</html>
```